New Business Card & Logo Design Project for PR Agency

Halvery & Partners Tech Public Relations agency is looking for a new business card design. Please see our website at www.halvery-pr.example for a description of our services. The design does not necessarily have to match the website’s aesthetic as we are looking for something fresh and modern that reflects our business. We want to emphasize that our focus is on media & public relations, content creation, social media and SEO. We want the business card to convey our BtoB technology focus and should have a very clean look. You are welcome to draw from our current halvery & partners logo on the card or play with that design too. We also like the idea of utilizing blue and white, which are often used in technology-related designs and layouts.
Attached are jpegs of the current logo and current card design for your reference.
Target Market(s)
Our clients are Business-to-Business technology providers.We sell our services to the CEO/President/Marketing director of a technology providing company.
Industry/Entity Type
Business
Look and feel

```html
<!DOCTYPE html>
<html lang="en">
<head>
<meta charset="utf-8">
<title>Halvery &amp; Partners — Business Card</title>
<link href="https://fonts.googleapis.com/css2?family=Arimo:wght@400;700&display=swap" rel="stylesheet">
<style>
  :root {
    --backdrop: #d9d8d5;
    --card-white: #fbfbfa;
    --card-black: #1f1f1f;
    --ink: #141414;
    --ink-soft: #2b2b2b;
    --accent-red: #d3151c;
    --rule: #9a9a9a;
    --paper-grey: #cfcfcf;
  }
  * { box-sizing: border-box; margin: 0; padding: 0; }
  html, body {
    width: 1200px; height: 900px; overflow: hidden;
    background: var(--backdrop);
    font-family: "Arimo", Arial, sans-serif;
  }
  .sheet {
    width: 1200px; height: 900px;
    display: flex; flex-direction: column;
    align-items: center; justify-content: center; gap: 60px;
  }
  .card {
    position: relative;
    width: 630px; height: 360px;
    border-radius: 28px;
    box-shadow: 0 6px 18px rgba(0,0,0,0.18);
  }

  /* Back side */
  .card--back {
    background: var(--card-black);
    color: #fff;
    display: flex; flex-direction: column; align-items: center; justify-content: center;
  }
  .card--back .wordmark { font-size: 30px; color: #fff; }
  .tagline {
    margin-top: 12px;
    font-size: 17px; color: #e6e6e6; letter-spacing: 0.3px;
  }
  .tagline .sep { color: var(--accent-red); margin: 0 6px; }
  .website {
    margin-top: 34px;
    font-size: 15px; font-weight: 700; color: #fff; letter-spacing: 0.4px;
  }

  /* Wordmark */
  .wordmark {
    font-weight: 700; letter-spacing: 0.5px; white-space: nowrap;
  }

  /* Front side */
  .card--front { background: var(--card-white); }
  .card--front .wordmark {
    position: absolute; left: 46px; top: 228px;
    font-size: 22px; color: var(--ink);
  }
  .divider {
    position: absolute; left: 352px; top: 30px;
    width: 1px; height: 230px; background: var(--rule);
  }
  .contact {
    position: absolute; left: 378px; top: 48px;
    color: var(--ink-soft);
  }
  .contact__name { font-size: 26px; font-weight: 700; color: var(--ink); line-height: 1.05; }
  .contact__title { font-size: 15px; color: var(--accent-red); margin-top: 3px; }
  .contact__address { font-size: 13.5px; line-height: 1.3; margin-top: 26px; }
  .contact__lines { list-style: none; margin-top: 3px; margin-left: 18px; }
  .contact__lines li {
    display: flex; align-items: center; gap: 6px;
    font-size: 13.5px; line-height: 1.3;
  }
  .icon { width: 14px; height: 12px; flex: none; fill: var(--accent-red); }
</style>
</head>
<body>
<main class="sheet">

  <section class="card card--front" aria-label="Card front">
    <div class="wordmark">halvery &amp; partners</div>
    <div class="divider"></div>
    <div class="contact">
      <p class="contact__name">Michael Doe</p>
      <p class="contact__title">President / CEO</p>
      <p class="contact__address">Street Address, Somewhere<br>Suite, City Name, State 00000</p>
      <ul class="contact__lines">
        <li>
          <svg class="icon" viewBox="0 0 14 12" aria-label="Phone"><path d="M1 4c0-2 2-3 6-3s6 1 6 3l-3 1-1-1.5H5L4 5zM3 6h8l2 5H1z"/></svg>
          (00) 000.000.000
        </li>
        <li>
          <svg class="icon" viewBox="0 0 14 12" aria-label="Fax"><path d="M4 0h6v4H4zM1 4h12v8H1zM3 7h8v1H3zM3 9h8v1H3z" fill-rule="evenodd"/></svg>
          (00) 000.000.000
        </li>
        <li>
          <svg class="icon" viewBox="0 0 14 12" aria-label="Mobile"><path d="M4 0h6a1 1 0 0 1 1 1v10a1 1 0 0 1-1 1H4a1 1 0 0 1-1-1V1a1 1 0 0 1 1-1zM5 2v5h4V2z" fill-rule="evenodd"/></svg>
          (00) 000.000.000
        </li>
        <li>
          <svg class="icon" viewBox="0 0 14 12" aria-label="Email"><path d="M0 2h14v9H0zM1 3l6 4 6-4v-.01H1z" fill-rule="evenodd"/></svg>
          michael@halvery-pr.example
        </li>
      </ul>
    </div>
  </section>

  <section class="card card--back" aria-label="Card back">
    <div class="wordmark">halvery &amp; partners</div>
    <p class="tagline">Tech PR<span class="sep">|</span>Content<span class="sep">|</span>Social Media</p>
    <p class="website">www.halvery-pr.example</p>
  </section>

</main>
</body>
</html>
```